Spice Mix Label Bottle Branding - Health and Weight Loss Mixes

The company is called ZestRow Spice Mix's. We've created 5 spice mixes using ingredients that promote health and weight loss. We already have a logo but now we need labels for our bottles. We would like to see designs that have the feel of health supplements (see attached examples)

We would like a different colour featured with each of our flavours.

Our flavours are:
-Golden Chai (Yellow)
-Mild Curry (Orange)
-Coffee Rub (brown)
-Garlic Oregano (Green)
-Taco (Blue)

Thank you!

Target Market(s)

Ages 22-35. Men and Female. Trendy, Hipster.

Industry/Entity Type

Food Production

Font styles to use
Sans Serif

Colors
f37122
0655a3
0692cd
9bcb3c
fbee3f

Requirements
Must have
• A different featured colour for each flavour.
• The ZestRow Spices Logo (attached)
• The slogan: "Weight Loss Ingredients"
• -Golden Chai (Yellow)
• -Mild Curry (Orange)
• -Coffee Rub (brown)
• -Garlic Oregano (Green)
• -Taco (Blue)
• Text Files attached.
Nice to have
• A black label with a featured colour for each of the spice mice flavours.
• 'No Salt added'

```html
<!DOCTYPE html>
<html lang="en">
<head>
<meta charset="utf-8">
<title>ZestRow Spices – Bottle Labels</title>
<link rel="stylesheet" href="https://fonts.googleapis.com/css2?family=Oswald:wght@500;700&display=swap">
<style>
  :root {
    --page: #ffffff;
    --panel: #1d1d1d;
    --panel-light: #262626;
    --ink: #ffffff;
    --taco: #2f6aa3;
    --coffee: #9c6433;
    --garlic: #97b836;
    --curry: #ee5a0f;
    --chai: #d99c28;
  }
  * { box-sizing: border-box; margin: 0; padding: 0; }
  html, body {
    width: 1200px;
    height: 504px;
    overflow: hidden;
    background: var(--page);
  }
  .label-row {
    position: relative;
    width: 1200px;
    height: 504px;
  }
  .label {
    position: absolute;
    top: 76px;
    width: 176px;
    height: 352px;
    color: var(--ink);
    font-family: "Oswald", sans-serif;
    text-align: center;
  }
  .label--taco   { left: 38px;  --accent: var(--taco); }
  .label--coffee { left: 278px; --accent: var(--coffee); }
  .label--garlic { left: 516px; --accent: var(--garlic); }
  .label--curry  { left: 755px; --accent: var(--curry); }
  .label--chai   { left: 993px; --accent: var(--chai); }

  .label__shape {
    position: absolute;
    inset: 0;
    width: 176px;
    height: 352px;
  }
  .label__frame { fill: var(--accent); }
  .label__panel { fill: url(#panelShade); }
  .label__rim { fill: none; stroke: var(--accent); stroke-opacity: .55; stroke-width: 1.5; filter: brightness(1.3); }

  .rule {
    position: absolute;
    left: 22px;
    width: 132px;
    height: 1px;
    background: var(--ink);
  }
  .rule--top { top: 55px; }
  .rule--bottom { top: 262px; left: 32px; width: 112px; }
  .rule__dots {
    position: absolute;
    left: 50%;
    top: -2px;
    transform: translateX(-50%);
    display: flex;
    gap: 2px;
    padding: 0 4px;
    background: var(--panel);
  }
  .rule__dots span {
    width: 4px; height: 4px;
    border-radius: 50%;
    background: var(--ink);
  }

  .brand {
    position: absolute;
    top: 60px;
    left: 0;
    width: 176px;
    font-weight: 700;
    color: var(--ink);
    text-transform: uppercase;
    line-height: 1;
  }
  .brand__name { display: block; font-size: 40px; letter-spacing: .5px; }
  .brand__sub { display: block; font-size: 10px; letter-spacing: 6px; margin-top: 4px; padding-left: 6px; }

  .slogan {
    position: absolute;
    top: 123px;
    width: 176px;
    font-size: 7.5px;
    font-weight: 700;
    text-transform: uppercase;
    letter-spacing: .2px;
  }
  .slogan-dots {
    position: absolute;
    top: 134px;
    left: 50%;
    transform: translateX(-50%);
    display: flex;
    gap: 2px;
  }
  .slogan-dots span { width: 3px; height: 3px; border-radius: 50%; background: var(--ink); }

  .flavour {
    position: absolute;
    top: 160px;
    height: 82px;
    left: 14px;
    width: 148px;
    display: flex;
    align-items: center;
    justify-content: center;
    font-size: 38px;
    line-height: 40px;
    font-weight: 700;
    text-transform: uppercase;
    color: var(--accent);
    letter-spacing: .5px;
  }
  .note {
    position: absolute;
    top: 271px;
    width: 176px;
    font-size: 11px;
    font-weight: 500;
    text-transform: uppercase;
  }
</style>
</head>
<body>
<svg width="0" height="0" style="position:absolute" aria-hidden="true">
  <defs>
    <linearGradient id="panelShade" x1="0" y1="0" x2="1" y2="1">
      <stop offset="0" stop-color="#262626"/>
      <stop offset="1" stop-color="#1a1a1a"/>
    </linearGradient>
    <symbol id="labelShape" viewBox="0 0 176 352">
      <path class="label__frame" d="M0,0 H176 V220 C176,300 122,338 88,352 C54,338 0,300 0,220 Z"/>
      <path class="label__panel" d="M12,0 H164 V218 C164,288 116,324 88,336 C60,324 12,288 12,218 Z"/>
    </symbol>
  </defs>
</svg>

<main class="label-row">
  <article class="label label--taco">
    <svg class="label__shape" aria-hidden="true"><use href="#labelShape"/></svg>
    <div class="rule rule--top"></div>
    <p class="brand"><span class="brand__name">ZestRow</span><span class="brand__sub">Spices</span></p>
    <p class="slogan">Weight Loss Seasonings</p>
    <div class="slogan-dots"><span></span><span></span><span></span></div>
    <h2 class="flavour">Taco</h2>
    <div class="rule rule--bottom"><div class="rule__dots"><span></span><span></span><span></span></div></div>
    <p class="note">No Salt Added</p>
  </article>

  <article class="label label--coffee">
    <svg class="label__shape" aria-hidden="true"><use href="#labelShape"/></svg>
    <div class="rule rule--top"></div>
    <p class="brand"><span class="brand__name">ZestRow</span><span class="brand__sub">Spices</span></p>
    <p class="slogan">Weight Loss Seasonings</p>
    <div class="slogan-dots"><span></span><span></span><span></span></div>
    <h2 class="flavour">Coffee<br>Rub</h2>
    <div class="rule rule--bottom"><div class="rule__dots"><span></span><span></span><span></span></div></div>
    <p class="note">No Salt Added</p>
  </article>

  <article class="label label--garlic">
    <svg class="label__shape" aria-hidden="true"><use href="#labelShape"/></svg>
    <div class="rule rule--top"></div>
    <p class="brand"><span class="brand__name">ZestRow</span><span class="brand__sub">Spices</span></p>
    <p class="slogan">Weight Loss Seasonings</p>
    <div class="slogan-dots"><span></span><span></span><span></span></div>
    <h2 class="flavour">Garlic<br>Oregano</h2>
    <div class="rule rule--bottom"><div class="rule__dots"><span></span><span></span><span></span></div></div>
    <p class="note">No Salt Added</p>
  </article>

  <article class="label label--curry">
    <svg class="label__shape" aria-hidden="true"><use href="#labelShape"/></svg>
    <div class="rule rule--top"></div>
    <p class="brand"><span class="brand__name">ZestRow</span><span class="brand__sub">Spices</span></p>
    <p class="slogan">Weight Loss Seasonings</p>
    <div class="slogan-dots"><span></span><span></span><span></span></div>
    <h2 class="flavour">Mild<br>Curry</h2>
    <div class="rule rule--bottom"><div class="rule__dots"><span></span><span></span><span></span></div></div>
    <p class="note">No Salt Added</p>
  </article>

  <article class="label label--chai">
    <svg class="label__shape" aria-hidden="true"><use href="#labelShape"/></svg>
    <div class="rule rule--top"></div>
    <p class="brand"><span class="brand__name">ZestRow</span><span class="brand__sub">Spices</span></p>
    <p class="slogan">Weight Loss Seasonings</p>
    <div class="slogan-dots"><span></span><span></span><span></span></div>
    <h2 class="flavour">Golden<br>Chai</h2>
    <div class="rule rule--bottom"><div class="rule__dots"><span></span><span></span><span></span></div></div>
    <p class="note">No Salt Added</p>
  </article>
</main>
</body>
</html>
```